Contemporary update for a market leader in foodservice distribution

KORLO is a market leader in foodservice distribution nationwide.
We have recently adopted a new look and feel for our flagship foodservice rewards programme, and we're looking to have our business cards reflect our new aesthetic. Below is a link to our new rewards website to give you a general idea on the look we're after. https://korlotierclub.com.au/

Industry/Entity Type

Distribution

Contact Information for Business Card

Must have space for contact name, position, company name and ABN, address, phone number and direct number, fax, email, and web address.

Font styles to use
Serif
Sans Serif

Requirements
Must have
• We'd like a landscape design, with our 'Bright Ember Tier' logo incorporated on either the front or the back of the card. The overall design should be contemporary and professional.
Nice to have
• I have included both the full colour and white version of our company logo - our preference is to have the company logo one solid colour (white, or a shade of grey) although we're also open to designs including the full colour logo. If you are able to incorporate a small Chatterleaf and Workmesh logo, please do so.
Should not have
• Should not have an over-complicated design. No images of globes, or food.

```html
<!DOCTYPE html>
<html lang="en">
<head>
<meta charset="utf-8">
<title>KORLO Business Card</title>
<link rel="stylesheet" href="https://fonts.googleapis.com/css2?family=Montserrat:wght@400;500;700;800&display=swap">
<style>
  :root {
    --bg: #e6e6e4;
    --card-white: #ffffff;
    --ink: #1d1d1b;
    --black: #0b0b0b;
    --ember-green: #1fa24a;
    --korlo-green: #18915a;
    --accent-yellow: #f3e500;
    --text-light: #ffffff;
    --text-muted: #444444;
  }
  * { box-sizing: border-box; margin: 0; padding: 0; }
  html, body {
    width: 1200px; height: 900px; overflow: hidden;
    background: var(--bg);
    font-family: "Montserrat", sans-serif;
  }
  .canvas {
    width: 1200px; height: 900px;
    display: flex; flex-direction: column; align-items: center; justify-content: center;
    gap: 56px;
  }
  .card {
    position: relative;
    width: 630px; height: 360px;
    border-radius: 22px;
    overflow: hidden;
    background: var(--card-white);
    box-shadow: 0 10px 28px rgba(0,0,0,0.18);
  }

  /* Front */
  .front-brand {
    position: absolute; left: 0; right: 0; top: 110px;
    display: flex; align-items: center; justify-content: center; gap: 16px;
  }
  .front-brand .brand-dot {
    width: 46px; height: 46px; border-radius: 50%;
    background: var(--ember-green);
  }
  .front-brand .brand-name {
    font-size: 44px; font-weight: 800; color: var(--ink);
    letter-spacing: -0.5px;
  }
  .front-tagline {
    position: absolute; left: 0; right: 0; top: 178px;
    text-align: center;
    font-size: 13px; font-weight: 700; letter-spacing: 2px;
    color: var(--ember-green);
  }
  .front-web {
    position: absolute; left: 0; right: 0; top: 228px;
    text-align: center;
    font-size: 20px; font-weight: 400; color: var(--ink); letter-spacing: 0.5px;
  }
  .front-web strong { color: var(--ember-green); font-weight: 700; }

  /* Back */
  .back-shape { position: absolute; inset: 0; }
  .company-block {
    position: absolute; left: 180px; top: 36px;
    display: flex; align-items: flex-start; gap: 14px;
  }
  .company-block .brand-dot {
    width: 58px; height: 58px; border-radius: 50%;
    background: var(--korlo-green); margin-top: 4px;
  }
  .company-name {
    font-size: 52px; font-weight: 500; color: var(--ink); line-height: 1; letter-spacing: 2px;
  }
  .company-sub {
    font-size: 9.5px; font-weight: 700; letter-spacing: 0.8px; color: var(--ink);
    margin-top: 6px;
  }
  .company-abn {
    font-size: 13px; color: var(--text-muted); margin-top: 4px; padding-left: 56px;
  }
  .company-abn span { color: var(--korlo-green); }

  .person {
    position: absolute; left: 30px; top: 246px; width: 280px;
    text-align: right; color: var(--text-light);
  }
  .person-name {
    font-size: 25px; font-weight: 800; color: var(--accent-yellow); letter-spacing: 0.5px;
    line-height: 1.1;
  }
  .person-role { font-size: 13px; letter-spacing: 1px; margin-top: 3px; }
  .person-address { font-size: 12.5px; line-height: 1.45; margin-top: 5px; }

  .contacts {
    position: absolute; left: 336px; top: 212px;
    list-style: none; color: var(--text-light);
    font-size: 13px; line-height: 1;
  }
  .contacts li { display: flex; align-items: center; gap: 9px; height: 21px; }
  .contacts svg { width: 12px; height: 12px; flex: none; }
</style>
</head>
<body>
<main class="canvas">

  <section class="card card-front">
    <div class="front-brand">
      <span class="brand-dot"></span>
      <span class="brand-name">Bright Ember Tier</span>
    </div>
    <p class="front-tagline">FOODSERVICE REWARDS</p>
    <p class="front-web">www.<strong>brightembertier</strong>.com</p>
  </section>

  <section class="card card-back">
    <svg class="back-shape" viewBox="0 0 630 360" preserveAspectRatio="none">
      <path d="M0 234 C 200 234, 430 170, 630 80 L630 360 L0 360 Z" fill="var(--black)"/>
      <path d="M0 227 C 200 227, 430 163, 630 73" fill="none" stroke="var(--accent-yellow)" stroke-width="5"/>
    </svg>

    <div class="company-block">
      <span class="brand-dot"></span>
      <div>
        <div class="company-name">KORLO</div>
        <div class="company-sub">AUSTRALIAN FOODSERVICE DISTRIBUTION</div>
        <div class="company-abn"><span>ABN:</span> 318 5046 7729</div>
      </div>
    </div>

    <div class="person">
      <div class="person-name">MARLA TENNANT</div>
      <div class="person-role">DIRECTOR</div>
      <div class="person-address">48 Harbourline Way<br>Kestrel Park VIC 3141</div>
    </div>

    <ul class="contacts">
      <li>
        <svg viewBox="0 0 12 12"><path d="M2 1h2l1 3-1.3 1a6 6 0 0 0 3.3 3.3L8 7l3 1v2a1 1 0 0 1-1 1A9 9 0 0 1 1 2a1 1 0 0 1 1-1z" fill="var(--accent-yellow)"/></svg>
        +61 3 5550 1824
      </li>
      <li>
        <svg viewBox="0 0 12 12"><rect x="3" y="0.5" width="6" height="11" rx="1.2" fill="var(--accent-yellow)"/><rect x="4.2" y="2" width="3.6" height="6.5" fill="var(--black)"/></svg>
        +61 3 5550 1830(Direct)
      </li>
      <li>
        <svg viewBox="0 0 12 12"><rect x="1" y="4" width="10" height="6" rx="1" fill="var(--accent-yellow)"/><rect x="3" y="1" width="6" height="4" fill="var(--accent-yellow)"/></svg>
        +61 3 5550 1899
      </li>
      <li>
        <svg viewBox="0 0 12 12"><rect x="1" y="2.5" width="10" height="7" fill="none" stroke="var(--accent-yellow)" stroke-width="1.3"/><path d="M1 2.5l5 4 5-4" fill="none" stroke="var(--accent-yellow)" stroke-width="1.3"/></svg>
        hello@brightembertier.com
      </li>
      <li>
        <svg viewBox="0 0 12 12"><circle cx="6" cy="6" r="5" fill="none" stroke="var(--accent-yellow)" stroke-width="1.3"/><path d="M1 6h10M6 1c-2.5 3-2.5 7 0 10M6 1c2.5 3 2.5 7 0 10" fill="none" stroke="var(--accent-yellow)" stroke-width="1"/></svg>
        www.brightembertier.com
      </li>
    </ul>
  </section>

</main>
</body>
</html>
```